Help me create an amazing cover for my first ebook!!

I am looking to have a modern and professional looking cover for my first ebook. It will be published through Borvex Quill Self Press and will need to follow their formatting and guidelines. I want the cover to have a modern and vibrant feel, that appeals to a millennial audience. This is a real estate book that is focused on a niche category catered to young professionals, so the idea would be to appeal to them.

Title:
The Twentysomething Playbook for Duplex Living

A Smart Property Buying Plan to Start Early, Cut Your Housing Costs (Sometimes to Zero), and Speed Up Your Path to Lasting Wealth.

Davin Osterlund

Target Market(s)

Real Estate investors, investors, millennials, young professionals, college educated, 20-40 years old.Financial freedom, finance.

Industry/Entity Type

Real Estate

Font styles to use
Sans Serif

Colors

Designer to choose colors to be used in the design.

Requirements
Must have
• Must follow the borvex quill self press format. I attached a screenshot of the details, it can also be found here: https://qsp.borvexbooks.example/en_US/help/topic/R481736025
• Must include this title:
• The Twentysomething Playbook for Duplex Living
• A Smart Property Buying Plan to Start Early, Cut Your Housing Costs (Sometimes to Zero), and Speed Up Your Path to Lasting Wealth.
• Davin Osterlund.
• I added examples of book covers I like to use as a guide, I also added some color pallette examples.
Nice to have
• Modern, clean design that's not too busy. Some sort of simple photo or illustration to incorporate in the cover along with the text would be nice.

```html
<!DOCTYPE html>
<html lang="en">
<head>
<meta charset="utf-8">
<title>The Twentysomething Playbook for Duplex Living</title>
<link rel="stylesheet" href="https://fonts.googleapis.com/css2?family=Anton&family=Oswald:wght@500&display=swap">
<style>
  :root {
    --paper: #f6e7b5;
    --paper-light: #fbf1cf;
    --title-blue: #1d2a8c;
    --title-red: #d8131b;
    --rule-blue: #2a2f86;
    --wash-violet: #8f6fc2;
    --wash-plum: #6a3f7a;
    --wash-brown: #a66f4c;
    --shadow: rgba(20, 10, 30, 0.55);
  }
  * { margin: 0; padding: 0; box-sizing: border-box; }
  html, body { width: 750px; height: 1200px; overflow: hidden; background: var(--paper); }
  .cover {
    position: relative;
    width: 750px;
    height: 1200px;
    overflow: hidden;
    background: linear-gradient(160deg, var(--paper-light) 0%, var(--paper) 55%, #f1dca4 100%);
  }
  .cover-art {
    position: absolute;
    left: 180px;
    top: 330px;
    width: 570px;
    height: 640px;
  }
  .author {
    position: absolute;
    top: 70px;
    right: 50px;
    font-family: "Anton", sans-serif;
    font-size: 34px;
    letter-spacing: 1px;
    color: var(--title-red);
    text-transform: uppercase;
  }
  .title {
    position: absolute;
    left: 48px;
    top: 120px;
    font-family: "Anton", sans-serif;
    font-weight: 400;
    text-transform: uppercase;
    line-height: 140px;
    text-shadow: 3px 4px 3px var(--shadow);
  }
  .title span { display: block; font-size: 118px; letter-spacing: 1px; }
  .title .title-blue { color: var(--title-blue); }
  .title .title-red { color: var(--title-red); }
  .title .title-long { font-size: 86px; }
  .rule {
    position: absolute;
    left: 36px;
    width: 676px;
    height: 6px;
    background: var(--rule-blue);
  }
  .rule-top { top: 958px; }
  .rule-bottom { top: 1164px; }
  .subtitle {
    position: absolute;
    left: 40px;
    top: 982px;
    width: 670px;
    text-align: center;
    font-family: "Oswald", sans-serif;
    font-weight: 500;
    font-size: 29px;
    line-height: 50px;
    text-transform: uppercase;
    color: var(--title-red);
    text-shadow: 0 0 3px #fff, 0 0 3px #fff;
  }
</style>
</head>
<body>
  <main class="cover">
    <svg class="cover-art" viewBox="0 0 570 640" role="img" aria-label="Watercolor sketch of a modern two-storey house with large windows in violet and brown tones">
      <defs>
        <radialGradient id="wash" cx="45%" cy="45%" r="60%">
          <stop offset="0%" stop-color="var(--wash-plum)" stop-opacity="0.85"/>
          <stop offset="45%" stop-color="var(--wash-violet)" stop-opacity="0.6"/>
          <stop offset="75%" stop-color="var(--wash-brown)" stop-opacity="0.35"/>
          <stop offset="100%" stop-color="var(--paper)" stop-opacity="0"/>
        </radialGradient>
      </defs>
      <rect width="570" height="640" fill="url(#wash)"/>
    </svg>

    <p class="author">Davin Osterlund</p>

    <h1 class="title">
      <span class="title-blue">The</span>
      <span class="title-blue title-long">Twentysomething</span>
      <span class="title-blue">Playbook</span>
      <span class="title-red">For Duplex</span>
      <span class="title-red">Living</span>
    </h1>

    <div class="rule rule-top"></div>
    <p class="subtitle">A Smart Property Buying Plan to Start Early, Cut Your Housing Costs (Sometimes to Zero), and Speed Up Your Path to Lasting Wealth</p>
    <div class="rule rule-bottom"></div>
  </main>
</body>
</html>
```